HOME IMPROVEMENT Business Card

I want a very unique business card. nothing typical and boring. Im open to you ideas. Ive seen cards with gold and silver or color foil and spot UV coatings. Im looking for something that looks cool and grabs attention. I like rounded corners but am open to all suggestions. We are a home improvement company and I will have a presentation folder printed and a catalog printed also and want to keep that same theme. I love the colors in our logo but I am open at looking at a 3rd color that would work with my logo. I hope that helps.
Card should include
Address
Phone
Fax
Email
Website
Target Market(s)
Home owners, people looking to remodel their home
Industry/Entity Type
Home Improvement
Contact Information for Business Card
2871 Maple Crest Avenue Unit 400
Des Plaines, Il 60093
Phone
Direct Line
Email
Website
Font styles to use
Other font styles liked:
- IM OPEN MINDED
Requirements
Must have
- High end quality look nothing boring I like rounded corners but am open minded
Nice to have
- WOW. I want something nice and impressive.
Should not have
- ??? Not sure

```html
<!DOCTYPE html>
<html lang="en">
<head>
<meta charset="utf-8">
<title>Ridgeline Renovations – Business Card</title>
<link href="https://fonts.googleapis.com/css2?family=Arimo:wght@400;700&display=swap" rel="stylesheet">
<style>
  :root {
    --navy: #1f2252;
    --green: #1aa64a;
    --paper: #fbfcfc;
    --ink: #1c1c1c;
    --backdrop: #e9eaea;
  }
  * { box-sizing: border-box; margin: 0; padding: 0; }
  html, body { width: 1200px; height: 810px; overflow: hidden; }
  body {
    background: var(--backdrop);
    font-family: "Arimo", Arial, sans-serif;
    position: relative;
  }
  .card {
    position: absolute;
    width: 520px;
    height: 297px;
    background: var(--paper);
    border-radius: 6px;
    box-shadow: 0 6px 18px rgba(0,0,0,0.18);
    overflow: hidden;
  }
  .card--front { left: 50px; top: 256px; }
  .card--back { left: 630px; top: 256px; }

  .brand-name {
    font-weight: 700;
    color: var(--navy);
    white-space: nowrap;
    display: flex;
    align-items: center;
    gap: 10px;
  }
  .brand-name .brand-dot {
    width: 14px; height: 14px;
    background: var(--green);
    display: inline-block;
  }
  .card--front .brand-name {
    position: absolute;
    left: 0; right: 0; top: 0; bottom: 0;
    justify-content: center;
    font-size: 36px;
  }
  .card--back .brand-name {
    position: absolute;
    left: 30px; top: 62px;
    font-size: 27px;
  }

  .divider {
    position: absolute;
    left: 0; right: 0; top: 150px;
    height: 1px;
    background: var(--green);
  }
  .contact-list {
    list-style: none;
    position: absolute;
    font-size: 14px;
    color: var(--ink);
  }
  .contact-list li { display: flex; align-items: center; gap: 9px; height: 20px; }
  .contact-list--left { left: 30px; top: 166px; }
  .contact-list--right { right: 30px; top: 86px; }
  .contact-list--right li { flex-direction: row-reverse; }
  .icon { width: 12px; height: 12px; flex: none; }

  .address-band {
    position: absolute;
    left: 0; right: 0; bottom: 0;
    height: 62px;
    background: var(--green);
    color: #fff;
    font-size: 15px;
    display: flex;
    align-items: center;
    justify-content: center;
  }
</style>
</head>
<body>

<section class="card card--front">
  <div class="brand-name"><span class="brand-dot"></span>Ridgeline Renovations</div>
</section>

<section class="card card--back">
  <div class="brand-name"><span class="brand-dot"></span>Ridgeline Renovations</div>

  <ul class="contact-list contact-list--right">
    <li>
      <svg class="icon" viewBox="0 0 12 12"><rect width="12" height="12" fill="#1aa64a"/><rect x="2.5" y="4" width="7" height="5" fill="none" stroke="#fff"/><rect x="4" y="2.5" width="4" height="2" fill="#fff"/></svg>
      <span>2671-555-0193</span>
    </li>
    <li>
      <svg class="icon" viewBox="0 0 12 12"><rect width="12" height="12" fill="#1aa64a"/><circle cx="6" cy="6" r="3.5" fill="none" stroke="#fff"/><line x1="2.5" y1="6" x2="9.5" y2="6" stroke="#fff"/><line x1="6" y1="2.5" x2="6" y2="9.5" stroke="#fff"/></svg>
      <span>www.ridgelinereno.com</span>
    </li>
  </ul>

  <div class="divider"></div>

  <ul class="contact-list contact-list--left">
    <li>
      <svg class="icon" viewBox="0 0 12 12"><rect width="12" height="12" fill="#1aa64a"/><path d="M3 2.5 L5 2.5 L5.5 4.5 L4.5 5.3 Q5.5 7 6.7 7.5 L7.5 6.5 L9.5 7 L9.5 9 Q5 9.5 3 3.5 Z" fill="#fff"/></svg>
      <span>415 555 0182</span>
    </li>
    <li>
      <svg class="icon" viewBox="0 0 12 12"><rect width="12" height="12" fill="#1aa64a"/><rect x="2.5" y="4" width="7" height="5" fill="none" stroke="#fff"/><rect x="4" y="2.5" width="4" height="2" fill="#fff"/></svg>
      <span>1-541-555-0147</span>
    </li>
    <li>
      <svg class="icon" viewBox="0 0 12 12"><rect width="12" height="12" fill="#1aa64a"/><rect x="2.5" y="3.5" width="7" height="5" fill="none" stroke="#fff"/><path d="M2.5 3.5 L6 6.5 L9.5 3.5" fill="none" stroke="#fff"/></svg>
      <span>hello@ridgelinereno.com</span>
    </li>
  </ul>

  <div class="address-band">2871 Maple Crest Avenue Unit 400 Des Plaines, Il 60093</div>
</section>

</body>
</html>
```